Business Card Design Project

We require a professional business card designed for our consulting organisation that has the same theme and colours as our logo except for the grey.

Colours on the front should predominately be white however some reference to our logo colours except for the grey.

The back of the card should be have background colour that aligns with our logo colour.

Layout, style and design is up to the designer. So send through your designs

Details are attached in the word document project brief.

Target Market(s)

Target market are large corporate organisations

Industry/Entity Type

Business

Requirements
Must have
• Content on the front must have:

Dean Halvorsen
Managing Director

P: 0417 285 394
E: Dean@brevolinkpartners.com
W: www.brevolinkpartners.com

Content on the back must have the words:
Alliances
Placement
Training
Support

Design Colours
Must align to our logo

```html
<!DOCTYPE html>
<html lang="en">
<head>
<meta charset="utf-8">
<title>Brevolink Partners – Business Card</title>
<link rel="stylesheet" href="https://fonts.googleapis.com/css2?family=Ubuntu:wght@400;500;700&display=swap">
<style>
  :root {
    --page-bg: #d4d4d4;
    --card-white: #f3f4f5;
    --blue-deep: #1a73b8;
    --blue-mid: #2590d0;
    --blue-light: #3ba8db;
    --text-white: #ffffff;
    --brand-blue: #2596d1;
    --card-shadow: rgba(0, 0, 0, 0.22);
  }
  * { box-sizing: border-box; margin: 0; padding: 0; }
  html, body {
    width: 1200px;
    height: 1023px;
    overflow: hidden;
  }
  body {
    background: var(--page-bg);
    font-family: "Ubuntu", sans-serif;
    position: relative;
  }
  .card {
    position: absolute;
    top: 352px;
    width: 540px;
    height: 320px;
    border-radius: 30px;
    overflow: hidden;
    box-shadow: 0 10px 24px var(--card-shadow);
  }
  .card--front { left: 40px; background: var(--card-white); }
  .card--back {
    left: 620px;
    background: radial-gradient(ellipse at 50% 45%, var(--blue-light) 0%, var(--blue-mid) 45%, var(--blue-deep) 100%);
    color: var(--text-white);
  }

  /* Front */
  .front__brand {
    position: absolute;
    left: 0; top: 0;
    width: 216px; height: 100%;
    display: flex;
    flex-direction: column;
    align-items: center;
    justify-content: center;
    gap: 14px;
  }
  .brand-dot {
    width: 54px; height: 54px;
    border-radius: 50%;
    background: var(--brand-blue);
  }
  .brand-name {
    color: var(--brand-blue);
    font-weight: 700;
    font-size: 26px;
    line-height: 1.1;
    text-align: center;
  }
  .front__panel {
    position: absolute;
    left: 216px; top: 0; right: 0; bottom: 0;
    background: radial-gradient(ellipse at 60% 40%, var(--blue-light) 0%, var(--blue-mid) 50%, var(--blue-deep) 100%);
    color: var(--text-white);
    padding: 44px 30px 0 38px;
  }
  .person__name { font-size: 25px; font-weight: 700; }
  .person__role { font-size: 15px; margin-top: 4px; }
  .contact-list {
    position: absolute;
    left: 0; bottom: 34px;
    list-style: none;
  }
  .contact-list li {
    display: flex;
    align-items: center;
    height: 27px;
    font-size: 16px;
  }
  .contact-icon {
    width: 30px; height: 24px;
    background: var(--card-white);
    border-radius: 0 7px 7px 0;
    display: flex;
    align-items: center;
    justify-content: center;
    margin-right: 10px;
  }
  .contact-icon svg { width: 15px; height: 15px; }
  .contact-list li + li { margin-top: 1px; }

  /* Back */
  .back__services {
    position: absolute;
    top: 36px; left: 0; right: 0;
    text-align: center;
    font-size: 17px;
    font-weight: 700;
    letter-spacing: 0.3px;
  }
  .back__brand {
    position: absolute;
    top: 120px; left: 0; right: 0;
    display: flex;
    align-items: center;
    justify-content: center;
    gap: 16px;
  }
  .back__brand .brand-dot { background: var(--text-white); width: 46px; height: 46px; }
  .back__brand .brand-name { color: var(--text-white); font-size: 34px; text-align: left; }
  .back__web {
    position: absolute;
    bottom: 38px; left: 0; right: 0;
    text-align: center;
    font-size: 15px;
  }
</style>
</head>
<body>
  <section class="card card--front" aria-label="Business card front">
    <div class="front__brand">
      <span class="brand-dot"></span>
      <span class="brand-name">Brevolink<br>Partners</span>
    </div>
    <div class="front__panel">
      <p class="person__name">Dean Halvorsen</p>
      <p class="person__role">Managing Director</p>
      <ul class="contact-list">
        <li>
          <span class="contact-icon">
            <svg viewBox="0 0 16 16" fill="none" stroke="#2590d0" stroke-width="1.6"><rect x="4" y="1.5" width="8" height="13" rx="1.5"/><line x1="7" y1="12" x2="9" y2="12"/></svg>
          </span>0417 285 394
        </li>
        <li>
          <span class="contact-icon">
            <svg viewBox="0 0 16 16" fill="none" stroke="#2590d0" stroke-width="1.6"><rect x="1.5" y="3.5" width="13" height="9" rx="1"/><polyline points="1.5,4 8,9 14.5,4"/></svg>
          </span>Dean@brevolinkpartners.com
        </li>
        <li>
          <span class="contact-icon">
            <svg viewBox="0 0 16 16" fill="none" stroke="#2590d0" stroke-width="1.4"><circle cx="8" cy="8" r="6.5"/><ellipse cx="8" cy="8" rx="2.8" ry="6.5"/><line x1="1.5" y1="8" x2="14.5" y2="8"/></svg>
          </span>www.brevolinkpartners.com
        </li>
      </ul>
    </div>
  </section>

  <section class="card card--back" aria-label="Business card back">
    <p class="back__services">Alliances • Placement • Training • Support</p>
    <div class="back__brand">
      <span class="brand-dot"></span>
      <span class="brand-name">Brevolink<br>Partners</span>
    </div>
    <p class="back__web">www.brevolinkpartners.com</p>
  </section>
</body>
</html>
```